New business card for a regional office of a US M&A company

We need business card for a finance company, office based in Hong Kong , our Head office is in US, our business is to Merge and acquires companies , the new office will be a regional office for the Asia Pacific region. We want to use the head office logo as attached ( but don't have to be exactly the same, can be a variation to it) as a base and then add Asia Pacific alongside the logo.
We would prefer to have be bilingual Eng + Chinese, although we don't really have Chinese company name .

Industry/Entity Type

Business

Contact Information for Business Card

Carla Beth Soren
 

VP,
APAC M&A Operations
Tovar Crest Asia Pacific Limited
 
Unit 1407, K82
27 Sai Lok Fung Road, 
Hong Kong 
 
M: +852 6481 2037
T : +852 2736 4100
F : +852 2736 4155
VOIP: 4813
 
cbsoren@tovarcrest.com

Font styles to use
Serif
Sans Serif

Colors

Designer to choose colors to be used in the design.

Requirements
Must have
• APAC Office

```html
<!DOCTYPE html>
<html lang="en">
<head>
<meta charset="utf-8">
<title>Tovar Crest Asia Pacific – Business Card</title>
<link rel="stylesheet" href="https://fonts.googleapis.com/css2?family=Open+Sans:wght@400;600;700&display=swap">
<style>
  :root {
    --backdrop: #3b3633;
    --card-white: #f7f7f5;
    --navy: #0d2a45;
    --brand-blue: #1da1d8;
    --text-grey: #4a4a4a;
    --mark-silver: #e9ebee;
  }
  * { margin: 0; padding: 0; box-sizing: border-box; }
  html, body {
    width: 1200px;
    height: 844px;
    overflow: hidden;
    background: var(--backdrop);
    font-family: "Open Sans", Arial, sans-serif;
  }
  .stage {
    position: relative;
    width: 1200px;
    height: 844px;
  }
  .card {
    position: absolute;
    top: 267px;
    width: 540px;
    height: 310px;
    border-radius: 3px;
    box-shadow: 0 10px 28px rgba(0,0,0,0.45);
  }
  .card--front { left: 40px; background: var(--card-white); }
  .card--back { left: 620px; background: var(--navy); }

  /* Front */
  .brand {
    position: absolute;
    top: 34px;
    left: 196px;
    display: flex;
    align-items: center;
    gap: 26px;
  }
  .brand__square {
    width: 52px;
    height: 52px;
    background: var(--navy);
    transform: rotate(45deg);
  }
  .brand__name {
    color: var(--brand-blue);
    font-weight: 700;
    line-height: 1;
    text-transform: uppercase;
  }
  .brand__name span { display: block; }
  .brand__name .line-1 { font-size: 30px; }
  .brand__name .line-2 { font-size: 21px; margin-top: 3px; }

  .voip {
    position: absolute;
    top: 118px;
    left: 30px;
    font-size: 14px;
    font-weight: 700;
    color: var(--navy);
  }
  .voip__number { color: var(--brand-blue); }

  .contact {
    position: absolute;
    top: 158px;
    left: 30px;
    color: var(--text-grey);
    font-size: 13px;
    line-height: 1.35;
  }
  .contact__name {
    font-size: 17px;
    font-weight: 700;
    color: var(--navy);
    text-transform: uppercase;
  }
  .contact__role { margin-bottom: 10px; }
  .contact__row { white-space: nowrap; }
  .contact__label { font-weight: 700; color: var(--navy); }
  .contact__sep { margin: 0 8px; color: var(--text-grey); }
  .contact__company {
    margin-top: 9px;
    font-size: 14px;
    font-weight: 700;
    color: var(--navy);
    text-transform: uppercase;
  }

  /* Back */
  .back-brand {
    position: absolute;
    inset: 0;
    display: flex;
    flex-direction: column;
    align-items: center;
    justify-content: center;
    gap: 46px;
  }
  .back-brand__square {
    width: 92px;
    height: 92px;
    background: var(--mark-silver);
    transform: rotate(45deg);
  }
  .back-brand__name {
    color: var(--brand-blue);
    font-weight: 700;
    font-size: 20px;
    letter-spacing: 0.5px;
    text-transform: uppercase;
  }
</style>
</head>
<body>
<main class="stage">
  <section class="card card--front" aria-label="Business card front">
    <div class="brand">
      <div class="brand__square" aria-hidden="true"></div>
      <div class="brand__name">
        <span class="line-1">Tovar Crest</span>
        <span class="line-2">Asia Pacific Ltd</span>
      </div>
    </div>

    <p class="voip">VOIP: <span class="voip__number">4813</span></p>

    <div class="contact">
      <p class="contact__name">Carla Beth Soren VP</p>
      <p class="contact__role">APAC M&amp;A Operations</p>
      <p class="contact__row"><span class="contact__label">P:</span> +852 2736 4100<span class="contact__sep">|</span><span class="contact__label">M:</span> +852 6481 2037</p>
      <p class="contact__row"><span class="contact__label">F:</span> +852 2736 4155<span class="contact__sep">|</span><span class="contact__label">E:</span> cbsoren@tovarcrest.com</p>
      <p class="contact__company">Tovar Crest Asia Pacific Ltd</p>
      <p class="contact__row">Unit 1407, K82 27 Sai Lok Fung Road,&nbsp; Hong Kong</p>
    </div>
  </section>

  <section class="card card--back" aria-label="Business card back">
    <div class="back-brand">
      <div class="back-brand__square" aria-hidden="true"></div>
      <p class="back-brand__name">Tovar Crest Asia Pacific</p>
    </div>
  </section>
</main>
</body>
</html>
```